FR banner

we need a banner design (36"x120" horizontal) that will be displayed on a local high school baseball field. My company ( Crestwell Prints Co) has been producing signage for the Fernmoor Ridge community since 2009. We would like to communicate that we do more than banners. The final design should include the slogan "Signs Shirts Swag" and our Logo.

Target Market(s)

companies, teams, events, shirt and other marketing items.

Industry/Entity Type

Sign, Print,

Font styles to use
Sans Serif

Requirements
Should not have
• no baseball content.

```html
<!DOCTYPE html>
<html lang="en">
<head>
<meta charset="utf-8">
<title>Crestwell Prints Co — Signs Shirts Swag Banner</title>
<link rel="stylesheet" href="https://fonts.googleapis.com/css2?family=Michroma&family=Oswald:wght@600;700&display=swap">
<style>
  :root {
    --page-bg: #dcdcdc;
    --banner-bg: #f1f1f1;
    --ink: #161616;
    --chevron-grey: #cfcfcf;
    --corner-grey: #d9d9d9;
    --photo-light: #e9e4da;
    --photo-mid: #bfc3c6;
    --photo-dark: #2d3338;
  }
  * { margin: 0; padding: 0; box-sizing: border-box; }
  html, body {
    width: 1200px;
    height: 1200px;
    overflow: hidden;
    background: var(--page-bg);
  }
  .canvas {
    width: 1200px;
    height: 1200px;
    display: flex;
    align-items: center;
    justify-content: center;
  }
  .banner {
    position: relative;
    width: 1120px;
    height: 336px;
    background: var(--banner-bg);
    overflow: hidden;
    box-shadow: 0 6px 24px rgba(0,0,0,0.18);
  }
  .banner-shapes {
    position: absolute;
    inset: 0;
    width: 100%;
    height: 100%;
  }
  .brand {
    position: absolute;
    left: 22px;
    top: 34px;
    display: flex;
    align-items: center;
    gap: 8px;
  }
  .brand-mark {
    width: 16px;
    height: 16px;
    background: var(--ink);
  }
  .brand-name {
    font-family: "Oswald", sans-serif;
    font-weight: 700;
    font-size: 17px;
    line-height: 1.05;
    color: var(--ink);
    text-transform: uppercase;
    width: 84px;
  }
  .headline {
    position: absolute;
    left: 146px;
    top: 58px;
    color: var(--ink);
  }
  .headline-top {
    font-family: "Oswald", sans-serif;
    font-weight: 700;
    font-size: 84px;
    line-height: 1;
    letter-spacing: -1px;
    transform: scaleX(0.88);
    transform-origin: left center;
    word-spacing: 6px;
  }
  .headline-main {
    font-family: "Michroma", sans-serif;
    font-size: 76px;
    line-height: 1;
    margin-top: 4px;
    letter-spacing: 2px;
    transform: scaleY(1.05);
    transform-origin: left top;
  }
  .tagline {
    font-family: "Michroma", sans-serif;
    font-size: 14.5px;
    letter-spacing: 1.2px;
    margin-top: 18px;
    white-space: nowrap;
  }
</style>
</head>
<body>
<main class="canvas">
  <section class="banner">
    <svg class="banner-shapes" viewBox="0 0 1338 400" preserveAspectRatio="none" aria-hidden="true">
      <defs>
        <linearGradient id="press-tones" x1="0" y1="0" x2="1" y2="1">
          <stop offset="0" stop-color="var(--photo-dark)"/>
          <stop offset="0.35" stop-color="var(--photo-mid)"/>
          <stop offset="0.7" stop-color="var(--photo-light)"/>
          <stop offset="1" stop-color="var(--photo-mid)"/>
        </linearGradient>
      </defs>
      <!-- corner accents, lower left -->
      <polygon points="0,170 40,178 0,195" fill="var(--corner-grey)"/>
      <polygon points="0,190 140,222 110,400 0,400" fill="var(--corner-grey)"/>
      <polygon points="0,270 40,280 18,400 0,400" fill="var(--ink)"/>
      <line x1="140" y1="228" x2="125" y2="400" stroke="var(--corner-grey)" stroke-width="3"/>
      <!-- grey chevron -->
      <polygon points="760,0 960,0 835,140 1040,400 850,400 650,140" fill="var(--chevron-grey)"/>
      <line x1="700" y1="70" x2="740" y2="20" stroke="var(--chevron-grey)" stroke-width="3"/>
      <line x1="740" y1="235" x2="920" y2="400" stroke="var(--chevron-grey)" stroke-width="3"/>
      <!-- black chevron frame -->
      <polygon points="910,0 1338,0 1338,400 1060,400 780,135" fill="var(--ink)"/>
      <!-- bottom right bar -->
      <polygon points="1190,382 1338,382 1338,400 1175,400" fill="var(--ink)"/>
    </svg>
    <svg class="banner-shapes" viewBox="0 0 1338 400" preserveAspectRatio="none" role="img" aria-label="Photo of a large-format printing press with rolls of colourful printed paper">
      <polygon points="940,10 1338,10 1338,400 1085,400 815,135" fill="url(#press-tones)"/>
    </svg>

    <div class="brand">
      <span class="brand-mark"></span>
      <span class="brand-name">Crestwell Prints Co</span>
    </div>

    <div class="headline">
      <h1 class="headline-top">SIGNS SHIRTS</h1>
      <p class="headline-main">SWAG</p>
      <p class="tagline">FERNMOOR RIDGE COMMUNITY SINCE 2009</p>
    </div>
  </section>
</main>
</body>
</html>
```